Online Psychiatry business - Business Card

I need a business card design. The target audience is busy professionals of any field (this therapy appeals best to 24-35 year olds). It involves psychiatry by tele-medicine (or video-conference). Nothing on it should be a giveaway that it's about mental health. Professional design with silver or gold as the primary colors appeals to me. The card must be as simple and as uncluttered as possible. Some color and flowing design on the edge of the card appeals to me.
CrestMindLink.com should probably appear in the center of the card and stand out, i.e. bold lettering, and easy to read, no cursive, but Ariel Black. Some where below this, should appear "Too Busy to Take Care of Yourself? Think again." Since this isn't office based, I don't think an office address is necessary and limits clutter.
Information that does need to appear is my name: Gerald Whitcombe, MD
General phone number: 541-876-2209. I'm hoping to get an 24-hour answering service soon so leave a little room for this. In addition I want to include two email addresses:
CrestMindLink@maildrop-box.com and CrestMind247@maildrop-box.com
Updates

I like the designs. I would like someone to put the website in bold in the center

 as most have been doing with a smaller font reminder nearby saying "No time" etc.
but I'd like to put my name down in the corner with the rest of the contact material.
Black print against a white or grey background appeals to me, with darker silver artwork near the sides (simple abstract, like wavy lines or something you can one up with that works. 
thanks

I ve tried to provide as much feedback as possible given my time limits, so if you have extra questions, please feel free to email. I tried to attach a file of a business card I really like but make be difficult to actually manufacture. I'm going to send you a link to the photo. The card has a pull tab. There is not much information on the outside. In fact, if you were to design the outside, I would just print : Too Busy to Take Care of Yourself? Think Again.

When you pull the tab the remaining information is on the bottom half of the card. Please don't use the color pink!!!!
http://www.layoutgallerypost.com/2009/05/100-clever-card-ideas/
It is the 39th photo on the list, about 2/3ds of the way down the page. It is titled: Faltenkästli

#7 and #16 have an appeal to me, except for the dot patterns
Hope this helps

I'm running out of time and energy. I 've been trying to give do down the list and give  individual feedback but I won't be able to do that anymore.

So if you have any specific questions, write me, and again thank you for all your effort!!

I know i received your files, including your zip files, Plonix,

but Gideon, did you send me the files including ZIP on project 5914386?
thanks

Target Market(s)

Working professionals and executive, attorneys, etc.

Industry/Entity Type

Business

Logo Text

Don't Have Time to Take Care of Yourself? Think Again.

Logo styles of interest
Pictorial/Combination Logo
Wordmark Logo
Other font styles liked:
• Ariel Black appeals to me the most

Requirements
Must have
• Want to emphasize that the website must be obvious, easily found (The CrestMindLink.com)
For that reason i'd like the card to be white, and minimal decoration on one or both sides just to add some style and color
Nice to have
• A Very uncluttered, elegant design, and something that makes it stick in your head-doesn't everyone want the last?
Should not have
• Nothing on the card that give it away that this is about psychiatry, such as brain or other symbol, but also nothing that gives it away as a medical business, such as a stethoscope or red cross or anything.

```html
<!DOCTYPE html>
<html lang="en">
<head>
<meta charset="utf-8">
<title>CrestMindLink.com — Business Card Design</title>
<link rel="stylesheet" href="https://fonts.googleapis.com/css2?family=Bebas+Neue&family=Oswald:wght@500&family=Jost:wght@400;500;700&display=swap">
<style>
  :root {
    --ink: #111111;
    --paper: #ffffff;
    --page: #ffffff;
    --heading: #333333;
    --rule: #333333;
    --label: #222222;
  }
  * { box-sizing: border-box; margin: 0; padding: 0; }
  html, body {
    width: 960px;
    height: 1200px;
    overflow: hidden;
    background: var(--page);
  }
  .sheet {
    position: relative;
    width: 960px;
    height: 1200px;
  }
  .sheet-title {
    position: absolute;
    top: 330px;
    left: 0;
    width: 100%;
    text-align: center;
    font-family: "Bebas Neue", "Oswald", sans-serif;
    font-size: 76px;
    line-height: 1;
    color: var(--heading);
    letter-spacing: 0.5px;
  }
  .sheet-domain {
    position: absolute;
    top: 412px;
    left: 0;
    width: 100%;
    text-align: center;
    font-family: "Jost", sans-serif;
    font-size: 32px;
    letter-spacing: 1px;
    color: var(--heading);
  }
  .sheet-rule {
    position: absolute;
    top: 474px;
    left: 397px;
    width: 156px;
    height: 3px;
    background: var(--rule);
  }
  .card {
    position: absolute;
    top: 530px;
    width: 432px;
    height: 242px;
    background: var(--ink);
    padding: 10px;
    display: flex;
    flex-direction: column;
  }
  .card--front { left: 24px; }
  .card--back { left: 502px; }
  .band-light {
    background: var(--paper);
    height: 74px;
    position: relative;
  }
  .band-dark {
    height: 76px;
    display: flex;
    align-items: center;
    justify-content: center;
    color: var(--paper);
    font-family: "Jost", sans-serif;
    text-align: center;
  }
  .band-light--contact { height: 72px; }
  .wordmark {
    position: absolute;
    left: 10px;
    bottom: 8px;
    font-family: "Oswald", "Bebas Neue", sans-serif;
    font-weight: 500;
    font-size: 21px;
    letter-spacing: -0.3px;
    color: var(--ink);
  }
  .doctor-name {
    font-size: 15px;
    letter-spacing: 1.6px;
    text-transform: uppercase;
  }
  .doctor-name strong { font-weight: 700; }
  .contact-row {
    position: absolute;
    left: 6px;
    display: flex;
    align-items: center;
    gap: 6px;
    font-family: "Jost", sans-serif;
    font-size: 13.5px;
    color: var(--ink);
    line-height: 1.05;
  }
  .contact-row--phone { top: 8px; }
  .contact-row--mail { top: 36px; }
  .contact-icon { width: 18px; height: 18px; flex: none; }
  .tagline {
    font-size: 14px;
    letter-spacing: 1.6px;
    text-transform: uppercase;
    line-height: 1.3;
  }
  .tagline strong { display: block; font-weight: 700; letter-spacing: 2px; }
  .card-label {
    position: absolute;
    top: 792px;
    width: 432px;
    text-align: center;
    font-family: "Jost", sans-serif;
    font-size: 24px;
    color: var(--label);
  }
  .card-label--front { left: 24px; }
  .card-label--back { left: 502px; }
</style>
</head>
<body>
<main class="sheet">
  <h1 class="sheet-title">Business Card Design</h1>
  <p class="sheet-domain">crestmindlink.com</p>
  <div class="sheet-rule"></div>

  <section class="card card--front" aria-label="Card front">
    <div class="band-light">
      <span class="wordmark">CRESTMINDLINK.COM</span>
    </div>
    <div class="band-dark">
      <p class="doctor-name">Gerald Whitcombe, <strong>MD</strong></p>
    </div>
    <div class="band-light band-light--contact">
      <div class="contact-row contact-row--phone">
        <svg class="contact-icon" viewBox="0 0 18 18" aria-hidden="true">
          <circle cx="9" cy="9" r="9" fill="#111"/>
          <path d="M6.2 4.3c.4-.2.8 0 1 .4l.8 1.6c.2.4.1.8-.2 1l-.7.5c.4 1 1.2 1.9 2.2 2.4l.5-.7c.3-.3.7-.4 1-.2l1.6.8c.4.2.5.6.4 1l-.4 1c-.2.4-.6.6-1 .6-3.2-.3-5.9-3-6.2-6.2 0-.4.2-.8.6-1z" fill="#fff"/>
        </svg>
        <span>(541) 876-2209</span>
      </div>
      <div class="contact-row contact-row--mail">
        <svg class="contact-icon" viewBox="0 0 18 18" aria-hidden="true">
          <circle cx="9" cy="9" r="9" fill="#111"/>
          <rect x="4.5" y="6" width="9" height="6.4" rx="0.6" fill="#fff"/>
          <path d="M4.8 6.4L9 9.6l4.2-3.2" fill="none" stroke="#111" stroke-width="0.9"/>
        </svg>
        <span>crestmindlink@maildrop-box.com<br>crestmind247@maildrop-box.com</span>
      </div>
    </div>
  </section>
  <p class="card-label card-label--front">{front}</p>

  <section class="card card--back" aria-label="Card back">
    <div class="band-light"></div>
    <div class="band-dark">
      <p class="tagline">Too busy to take care of yourself?<strong>Think again.</strong></p>
    </div>
    <div class="band-light band-light--contact"></div>
  </section>
  <p class="card-label card-label--back">{back}</p>
</main>
</body>
</html>
```